Personal Business Card

I am an award winning banjo player who plays with two different professional bands. My experiences include studio recordings for other artists and played the theme song for the Creature Channel's "Frontier Tundra Nights". I am ready to take my career to the next level and would like something that will look professional. it is important to me to have a banjo on the card. If possible my accomplishments to be put on back of card.

Industry/Entity Type

Artists

Contact Information for Business Card

Morgan Pell
cell 602-315-2860
email morganpellbanjo@quillpost.net

2008 AZ Banjo Champion
2008 Pinemeadow Banjo Champion
2010 AZ Banjo Champion
2010 Copper Creek Gathering Halvorn Banjo Champion
2010 Birchstone Hollow Fair Banjo Finalist

```html
<!DOCTYPE html>
<html lang="en">
<head>
<meta charset="utf-8">
<title>Morgan Pell — Business Card</title>
<link rel="stylesheet" href="https://fonts.googleapis.com/css2?family=Quicksand:wght@300;400&family=Sacramento&display=swap">
<style>
  :root {
    --backdrop: #e9e7e4;
    --card-light: #fbfbfb;
    --card-dark: #3b3b3b;
    --ink: #1f1f1f;
    --ink-soft: #3a3a3a;
    --chalk: #f4f4f4;
    --ornament-tone: #d9d9d9;
    --illustration-tone: #6a6a6a;
  }
  * { box-sizing: border-box; margin: 0; padding: 0; }
  html, body {
    width: 1200px; height: 873px; overflow: hidden;
    background: var(--backdrop);
  }
  .sheet {
    width: 1200px; height: 873px;
    display: flex; align-items: center; justify-content: center; gap: 40px;
  }
  .card {
    width: 540px; height: 309px; position: relative;
    box-shadow: 0 2px 10px rgba(0,0,0,0.12);
  }

  /* Contact side */
  .card--contact { background: var(--card-light); color: var(--ink); font-family: "Quicksand", sans-serif; }
  .note-border {
    position: absolute; top: 14px; bottom: 14px; width: 40px;
    background: linear-gradient(180deg, var(--ornament-tone), #ececec, var(--ornament-tone));
    border-radius: 4px;
  }
  .note-border--left { left: 14px; }
  .note-border--right { right: 14px; }
  .contact-block {
    position: absolute; left: 70px; right: 70px; top: 40px;
    text-align: center;
  }
  .contact-name { font-weight: 300; font-size: 38px; letter-spacing: 0.5px; margin-bottom: 14px; }
  .contact-line {
    display: flex; align-items: center; justify-content: center; gap: 7px;
    font-size: 14px; font-weight: 400; color: var(--ink-soft); line-height: 22px;
  }
  .contact-line svg { width: 13px; height: 13px; flex: none; }
  .awards { list-style: none; margin-top: 16px; font-size: 13.5px; line-height: 20px; color: var(--ink-soft); }

  /* Brand side */
  .card--brand { background: var(--card-dark); color: var(--chalk); }
  .banjo-art {
    position: absolute; left: 150px; top: 34px; width: 240px; height: 84px;
    background: linear-gradient(90deg, var(--illustration-tone), #555 70%, var(--illustration-tone));
    border-radius: 42px 14px 14px 42px;
  }
  .brand-name {
    position: absolute; left: 0; right: 0; top: 130px; text-align: center;
    font-family: "Sacramento", cursive; font-size: 92px; line-height: 1;
  }
</style>
</head>
<body>
<main class="sheet">
  <section class="card card--contact" aria-label="Contact side">
    <div class="note-border note-border--left" role="img" aria-label="Column of music notes and treble clefs"></div>
    <div class="note-border note-border--right" role="img" aria-label="Column of music notes and treble clefs"></div>
    <div class="contact-block">
      <h1 class="contact-name">Morgan Pell</h1>
      <p class="contact-line">
        <svg viewBox="0 0 24 24" aria-hidden="true"><path fill="currentColor" d="M6.6 10.8a15.1 15.1 0 0 0 6.6 6.6l2.2-2.2c.3-.3.7-.4 1-.2 1.1.4 2.3.6 3.6.6.6 0 1 .4 1 1V20c0 .6-.4 1-1 1A17 17 0 0 1 3 4c0-.6.4-1 1-1h3.5c.6 0 1 .4 1 1 0 1.3.2 2.5.6 3.6.1.3 0 .7-.2 1z"/></svg>
        602-315-2860
      </p>
      <p class="contact-line">
        <svg viewBox="0 0 24 24" aria-hidden="true"><rect x="2" y="5" width="20" height="14" fill="none" stroke="currentColor" stroke-width="2"/><path d="M2 5l10 8 10-8M2 19l7-7M22 19l-7-7" fill="none" stroke="currentColor" stroke-width="2"/></svg>
        morganpellbanjo@quillpost.net
      </p>
      <ul class="awards">
        <li>(2008) AZ Banjo Champion</li>
        <li>Pinemeadow Banjo Champion</li>
        <li>(2010) AZ Banjo Champion</li>
        <li>Copper Creek Gathering Halvorn Banjo Champion</li>
      </ul>
    </div>
  </section>

  <section class="card card--brand" aria-label="Name side">
    <div class="banjo-art" role="img" aria-label="Line drawing of a banjo"></div>
    <p class="brand-name">Morgan Pell.</p>
  </section>
</main>
</body>
</html>
```